Business Cards and Stationary For Home Automation Company
based on recently completed logo
Business Cards and Stationary For Home Automation Company  - Manufacturing
Creative Brief
Professional
Milo Brandt
VP - Product and Business Development
717 Larkfield Crest Avenue Suite K310 Piscataway, NJ 08821
milo@mybrightwaterdwellingtech.com
www.MyBrightwaterDwellingTech.com

```html
<!DOCTYPE html>
<html lang="en">
<head>
<meta charset="utf-8">
<title>Brightwater Dwelling Tech — Business Card</title>
<link rel="stylesheet" href="https://fonts.googleapis.com/css2?family=Archivo:wght@400;600;800&display=swap">
<style>
  :root {
    --ground: #e9e9e7;
    --card: #ffffff;
    --ink: #161616;
    --green: #6cc832;
    --green-dark: #3f9a1c;
    --muted: #7a7a7a;
    --on-dark: #f2f2f2;
  }
  * { box-sizing: border-box; margin: 0; padding: 0; }
  html, body { width: 1200px; height: 901px; overflow: hidden; }
  body {
    background: var(--ground);
    font-family: "Archivo", Arial, sans-serif;
    position: relative;
  }
  .card {
    position: absolute;
    top: 296px;
    width: 540px;
    height: 309px;
    border-radius: 26px;
    background: var(--card);
    overflow: hidden;
    box-shadow: 0 10px 28px rgba(0,0,0,0.18);
  }
  .card--front { left: 40px; }
  .card--back { left: 620px; }

  .contact-panel {
    position: absolute; left: 0; right: 0; bottom: 0; height: 150px;
    background: var(--ink);
  }
  .accent-band {
    position: absolute; left: 0; right: 0; bottom: 150px; height: 8px;
    background: var(--green);
  }

  .brand { position: absolute; display: flex; align-items: center; gap: 12px; }
  .brand__mark { width: 34px; height: 34px; background: var(--ink); flex: none; }
  .brand__name {
    font-weight: 800; font-size: 25px; line-height: 0.95; color: var(--ink);
    letter-spacing: -0.3px;
  }
  .brand__tag {
    position: absolute; font-size: 8.5px; letter-spacing: 3px; color: var(--muted);
    font-weight: 600;
  }
  .card--front .brand { left: 34px; top: 30px; }
  .card--front .brand__tag { left: 34px; top: 105px; }
  .card--back .brand { left: 150px; top: 112px; }
  .card--back .brand__tag { left: 150px; top: 188px; }

  .person { position: absolute; right: 34px; top: 66px; text-align: right; }
  .person__name { font-size: 15px; font-weight: 600; color: var(--ink); letter-spacing: 0.5px; text-transform: uppercase; }
  .person__title { font-size: 9px; color: var(--green-dark); margin-top: 3px; }

  .contact {
    position: absolute; right: 30px; bottom: 22px; width: 280px;
    list-style: none; color: var(--on-dark); font-size: 10px; text-align: right;
  }
  .contact li { display: flex; justify-content: flex-end; align-items: center; gap: 7px; margin-top: 5px; }
  .contact .address { display: block; line-height: 1.35; margin-bottom: 3px; }
  .contact svg { width: 10px; height: 10px; fill: var(--on-dark); flex: none; }
</style>
</head>
<body>
  <section class="card card--front">
    <div class="accent-band"></div>
    <div class="contact-panel"></div>
    <div class="brand">
      <span class="brand__mark"></span>
      <span class="brand__name">Brightwater<br>Dwelling<br>Tech</span>
    </div>
    <span class="brand__tag">SMARTER LIVING SPACES</span>
    <div class="person">
      <p class="person__name">Milo Brandt</p>
      <p class="person__title">VP - Product and Business Development</p>
    </div>
    <ul class="contact">
      <li class="address">717 Larkfield Crest Avenue Suite K310<br>Piscataway, NJ 08821</li>
      <li>555 014 2290
        <svg viewBox="0 0 24 24"><path d="M6.6 10.8a15 15 0 0 0 6.6 6.6l2.2-2.2c.3-.3.7-.4 1-.2 1.1.4 2.3.6 3.6.6.6 0 1 .4 1 1V20c0 .6-.4 1-1 1A17 17 0 0 1 3 4c0-.6.4-1 1-1h3.5c.6 0 1 .4 1 1 0 1.3.2 2.5.6 3.6.1.3 0 .7-.2 1z"/></svg>
      </li>
      <li>555 014 2291
        <svg viewBox="0 0 24 24"><rect x="3" y="6" width="18" height="13" rx="1"/><rect x="7" y="2" width="10" height="5"/></svg>
      </li>
      <li>milo@mybrightwaterdwellingtech.com
        <svg viewBox="0 0 24 24"><rect x="2" y="5" width="20" height="14" rx="1"/></svg>
      </li>
      <li>www.MyBrightwaterDwellingTech.com
        <svg viewBox="0 0 24 24"><circle cx="12" cy="12" r="10"/></svg>
      </li>
    </ul>
  </section>

  <section class="card card--back">
    <div class="brand">
      <span class="brand__mark"></span>
      <span class="brand__name">Brightwater<br>Dwelling<br>Tech</span>
    </div>
    <span class="brand__tag">SMARTER LIVING SPACES</span>
  </section>
</body>
</html>
```